Lantern Marketing Group (LMG)

This is for my business cards. I want a Nice anfd Elegant Business Card to be Designed, Using more or less of the same colors of my logo that i have attached.i would like to have these business cards forever

Thank you

Thank you

Thank you

Contact Information for Business Card

Tobias Rennard
Lantern Marketing Group
C.(555) 214-6083
E-Mail. TRennard@lanternmgroup.example

Font styles to use
Serif
Sans Serif

Colors
d0dfed
cbcbcb
cee9f5

Requirements
Must have
• (LMG)
• Lantern Marketing Group
Nice to have
• 3D affects
Should not have
• Please try not using the flat version of the logo try and use the 3d version please

```html
<!DOCTYPE html>
<html lang="en">
<head>
<meta charset="utf-8">
<title>Lantern Marketing Group – Business Card</title>
<link rel="stylesheet" href="https://fonts.googleapis.com/css2?family=Open+Sans:wght@400;600;700&display=swap">
<style>
  :root {
    --brand-blue: #1f75c4;
    --ink-grey: #8a8a8a;
    --card-white: #ffffff;
    --card-grey: #e3e3e3;
    --rule-grey: #bdbdbd;
    --backdrop: #2b2b2b;
  }
  * { box-sizing: border-box; margin: 0; padding: 0; }
  html, body { width: 1200px; height: 787px; overflow: hidden; }
  body {
    background: var(--backdrop);
    font-family: "Open Sans", Arial, sans-serif;
    position: relative;
  }
  .card {
    position: absolute;
    top: 245px;
    width: 520px;
    height: 297px;
    overflow: hidden;
  }
  .card--front { left: 60px; background: var(--card-white); }
  .card--back  { left: 620px; background: var(--card-grey); }

  .band {
    position: absolute; left: 0; right: 0;
    height: 14px; background: var(--brand-blue);
  }
  .band--top { top: 0; }
  .band--bottom { bottom: 0; }
  .band-rule {
    position: absolute; left: 0; right: 0;
    height: 4px; background: var(--rule-grey);
  }
  .band-rule--top { top: 20px; }
  .band-rule--bottom { bottom: 20px; }

  .wordmark {
    display: flex; flex-direction: column; align-items: center;
    color: var(--brand-blue); font-weight: 700; text-transform: uppercase;
    text-align: center; line-height: 1.1;
  }
  .wordmark__square {
    width: 60px; height: 60px; background: var(--brand-blue); margin-bottom: 12px;
  }
  .card--front .wordmark {
    position: absolute; left: 0; right: 0; top: 72px;
    font-size: 26px; letter-spacing: 1px;
  }
  .card--back .wordmark {
    position: absolute; left: 22px; top: 86px; width: 200px;
    font-size: 17px;
  }
  .card--back .wordmark__square { width: 48px; height: 48px; margin-bottom: 10px; }

  .divider {
    position: absolute; left: 238px; top: 86px;
    width: 1px; height: 118px; background: var(--ink-grey);
  }
  .contact {
    position: absolute; left: 262px; top: 92px; width: 236px;
  }
  .contact__name {
    color: var(--brand-blue); font-size: 21px; font-weight: 700; line-height: 1.2;
  }
  .contact__role { color: var(--ink-grey); font-size: 13px; margin-top: 2px; }
  .contact__rule { height: 1px; background: var(--card-white); margin: 12px 0 12px; }
  .contact__line {
    display: flex; align-items: center; gap: 8px;
    color: var(--brand-blue); font-size: 13px; line-height: 1.6;
  }
  .contact__line svg { flex: none; }
</style>
</head>
<body>
  <section class="card card--front" aria-label="Card front">
    <div class="band band--top"></div>
    <div class="band-rule band-rule--top"></div>
    <div class="wordmark">
      <span class="wordmark__square" aria-hidden="true"></span>
      <span>Lantern Marketing Group</span>
    </div>
    <div class="band-rule band-rule--bottom"></div>
    <div class="band band--bottom"></div>
  </section>

  <section class="card card--back" aria-label="Card back">
    <div class="band band--top"></div>
    <div class="band-rule band-rule--top"></div>
    <div class="wordmark">
      <span class="wordmark__square" aria-hidden="true"></span>
      <span>Lantern Marketing Group</span>
    </div>
    <div class="divider"></div>
    <div class="contact">
      <p class="contact__name">Tobias Rennard</p>
      <p class="contact__role">Owner</p>
      <div class="contact__rule"></div>
      <p class="contact__line">
        <svg width="13" height="13" viewBox="0 0 24 24" aria-hidden="true"><path fill="#6d6d6d" d="M6.6 10.8a15.1 15.1 0 0 0 6.6 6.6l2.2-2.2a1 1 0 0 1 1-.25 11.4 11.4 0 0 0 3.6.57 1 1 0 0 1 1 1V20a1 1 0 0 1-1 1A17 17 0 0 1 3 4a1 1 0 0 1 1-1h3.5a1 1 0 0 1 1 1c0 1.25.2 2.45.57 3.57a1 1 0 0 1-.25 1z"/></svg>
        (555) 214-6083
      </p>
      <p class="contact__line">
        <svg width="13" height="11" viewBox="0 0 24 18" aria-hidden="true"><rect x="1" y="1" width="22" height="16" fill="none" stroke="#6d6d6d" stroke-width="2"/><path d="M1 1l11 9 11-9" fill="none" stroke="#6d6d6d" stroke-width="2"/></svg>
        TRennard@lanternmgroup.example
      </p>
    </div>
    <div class="band-rule band-rule--bottom"></div>
    <div class="band band--bottom"></div>
  </section>
</body>
</html>
```